Life Coaching and Career Coaching company needs new website with bold, modern, videos

We need a whole new website that is heavy on video. We are a small company who sells personal wellbeing services like career coaching, life coaching, and group coaching programs. The programs all help people design a better life.
FULL BRIEF ATTACHED and STYLE GUIDE
Also, look at https://www.brightfennel.com/coaching and galdrove.com and https://www.marnwick.life/ for a small amount of inspiration.

Industry/Entity Type

personal well-being/life coaching/career coaching

Number of Pages Required

3 page

Other font styles liked:
• fonts are in the brief

Requirements
Must have
• read the brief please - it's all in there. (things like the look, feel, how it will have lots of video, etc,)
Nice to have
• something really different looking and breakthrough. visually stunning. very trustworthy. Please read the brief, its all in there.
Should not have
• should not look like other life coaching websites. must have video!

```html
<!DOCTYPE html>
<html lang="en">
<head>
<meta charset="utf-8">
<title>Lumen Life Lab</title>
<link rel="stylesheet" href="https://fonts.googleapis.com/css2?family=Outfit:wght@300;400;500;600;700&family=Nunito+Sans:ital,wght@0,400;0,600;0,700;1,400&family=Cormorant+Garamond:wght@500&display=swap">
<style>
:root{
  --coral:#f2635b;
  --coral-soft:#f7a39d;
  --pink:#fde8e6;
  --pink-2:#fce3e1;
  --teal:#005a55;
  --ink:#1c1c1c;
  --body:#333;
  --muted:#8a8a8a;
  --page:#f9f9f9;
  --white:#fff;
}
*{box-sizing:border-box;margin:0;padding:0}
html,body{width:1200px;height:2898px;overflow:hidden}
body{position:relative;background:var(--page);font-family:"Nunito Sans",sans-serif;color:var(--body)}
.abs{position:absolute}
.brand{font-family:"Outfit",sans-serif;font-weight:400;color:#6d6d6d;letter-spacing:1px;display:flex;align-items:center;gap:10px}
.brand .dot{width:14px;height:14px;background:#6d6d6d}

/* header */
.site-header{left:0;top:0;width:1200px;height:124px;background:var(--pink)}
.site-header .brand{position:absolute;left:82px;top:38px;font-size:36px}
.nav{position:absolute;left:455px;top:52px;display:flex;gap:35px;font-size:17px;color:var(--ink)}
.btn{display:flex;align-items:center;justify-content:center;font-family:"Nunito Sans",sans-serif;color:var(--white);background:var(--coral)}
.header-cta{position:absolute;left:942px;top:42px;width:175px;height:44px;border-radius:4px;font-size:17px}

/* hero */
.hero{left:0;top:124px;width:1200px;height:470px;background:linear-gradient(180deg,#f6f1ef,#f8f4f2)}
.eyebrow{left:83px;top:160px;font-family:"Cormorant Garamond",serif;font-size:25px;color:var(--coral)}
.hero-title{left:83px;top:190px;width:560px;font-family:"Outfit",sans-serif;font-weight:600;font-size:50px;line-height:65px;color:var(--ink)}
.hero-title em{font-style:normal;color:var(--coral)}
.hero-copy{left:83px;top:397px;width:450px;font-size:19px;line-height:26.5px;color:#333}
.pill{position:absolute;top:518px;height:47px;border-radius:24px;font-size:14px}
.pill.solid{left:83px;width:160px}
.pill.outline{left:257px;width:152px;background:transparent;color:var(--coral);border:2px solid var(--coral)}
.hero-media{left:621px;top:187px;width:487px;height:323px;background:linear-gradient(135deg,#8a5a35,#c98a3a 45%,#4f6a8a);box-shadow:0 6px 24px rgba(0,0,0,.12)}
.play{position:absolute;border-radius:50%;background:var(--coral)}
.play svg{position:absolute;left:0;top:0;width:100%;height:100%}

/* about */
.video-frame{left:96px;top:707px;width:519px;height:362px;background:#050505;border-radius:8px}
.video-frame .screen{position:absolute;left:36px;top:106px;width:450px;height:143px;background:linear-gradient(90deg,#9a7a5a,#b39b80 45%,#5f6b70 55%,#7a8088)}
.section-title{font-family:"Outfit",sans-serif;font-weight:500;font-size:29px;color:var(--ink)}
.rule{height:4px;border-radius:2px;background:var(--coral)}
.about-copy{left:675px;top:747px;width:440px;font-size:16.5px;line-height:23px;color:#222}
.feature{left:675px;display:flex;align-items:center;gap:14px;font-size:13.5px;color:#222}
.feature .icon{width:38px;height:38px;border:1.5px solid var(--coral-soft);border-radius:6px;background:#fdeceb}
.explore{left:675px;top:1050px;width:138px;height:45px;border-radius:2px;font-size:14px}

/* products */
.products{left:0;top:1180px;width:1200px;height:563px;background:var(--pink-2)}
.products-title{left:0;top:1213px;width:1200px;text-align:center;font-family:"Outfit",sans-serif;font-weight:600;font-size:29px;color:var(--coral)}
.card{position:absolute;top:1313px;width:358px;height:396px;background:var(--white);border-radius:8px;box-shadow:0 4px 14px rgba(0,0,0,.08);text-align:center;font-family:"Outfit",sans-serif}
.card h3{margin-top:18px;font-weight:500;font-size:29px;color:var(--ink)}
.card .desc{margin-top:6px;font-family:"Nunito Sans",sans-serif;font-style:italic;font-size:16.5px;line-height:23px;color:#444}
.card .was{margin-top:28px;font-size:16px;color:#999}
.card .was s{margin-right:8px}
.save{display:inline-block;padding:1px 6px;border-radius:10px;background:#e3f5f3;color:var(--teal);font-weight:500}
.card .from{margin-top:8px;font-size:17px;color:#666}
.price{font-size:46px;font-weight:600;color:var(--teal);line-height:48px}
.price small{font-size:17px;font-weight:600}
.free{margin-top:22px;font-size:17px;font-weight:500;color:var(--teal)}
.benefit{margin:16px auto 0;width:268px;height:46px;font-family:"Outfit",sans-serif;font-size:23px;background:var(--teal);border-radius:2px}
.more{margin-top:14px;font-size:16.5px;color:#999}
.card.featured .save{background:#fde6e4;color:var(--coral)}
.card.featured .price,.card.featured .free{color:var(--coral)}
.card.featured .benefit{background:var(--coral)}
.badge{position:absolute;left:529px;top:1296px;width:142px;height:34px;border-radius:14px;background:var(--coral);color:var(--white);font-family:"Outfit",sans-serif;font-size:22px;display:flex;align-items:center;justify-content:center;z-index:2}

/* testimonials */
.testi{position:absolute;display:flex;align-items:flex-end;justify-content:center;text-align:center;color:var(--white);font-family:"Outfit",sans-serif;font-weight:500;font-size:20px;line-height:26px}
.testi p{margin-bottom:26px;padding:0 24px;text-shadow:0 1px 4px rgba(0,0,0,.4)}
.arrow{position:absolute;top:2372px;width:43px;height:43px;border:1.5px solid #222;border-radius:50%}
.dots{left:574px;top:2390px;display:flex;gap:5px;align-items:center}
.dots span{width:6px;height:6px;border-radius:50%;background:#ddd}
.dots span.on{width:26px;border-radius:3px;background:var(--coral)}

/* cta */
.cta{left:0;top:2497px;width:1200px;height:146px;background:var(--white);border-top:2px solid var(--coral-soft)}
.cta-text{left:141px;top:2528px;font-family:"Outfit",sans-serif;font-size:31px;line-height:42px;color:var(--coral)}
.cta-text strong{font-weight:700}
.cta-btn{left:848px;top:2546px;width:223px;height:50px;border-radius:6px;font-size:16px}

/* footer */
.site-footer{left:0;top:2643px;width:1200px;height:255px;background:var(--pink)}
.site-footer .brand{position:absolute;left:0;top:2682px;width:1200px;justify-content:center;font-size:38px}
.foot-nav{left:0;top:2761px;width:1200px;display:flex;justify-content:center;gap:22px;font-size:14px;color:#222}
.social{left:944px;top:2814px;display:flex;gap:17px}
.social span{width:14px;height:14px;border-radius:50%;background:#555}
.foot-rule{left:117px;top:2837px;width:966px;height:1px;background:#777}
.copy{left:0;top:2858px;width:1200px;text-align:center;font-size:11px;color:#555}
</style>
</head>
<body>

<header class="abs site-header">
  <div class="brand"><span class="dot"></span>LUMEN LIFE LAB</div>
  <nav class="nav"><span>About Us</span><span>Our Services</span><span>Testimonials</span><span>Contact Us</span></nav>
  <a class="btn header-cta">Request a Demo</a>
</header>

<section class="abs hero"></section>
<div class="abs eyebrow">Lumen Life Lab</div>
<h1 class="abs hero-title">Achieve your best lives, both <em>Personally</em> and <em>Professionally</em> careers</h1>
<p class="abs hero-copy">Lorem ipsum dolor sit amet consectetur. Tempus facilisis est in magna eu ipsum at id nec. Urna scelerisque morbi fringilla pharetra. Nisi amet volutpat sapien elementum sit. Tincidunt.</p>
<a class="btn pill solid">Request a Demo</a>
<a class="btn pill outline">For Individuals</a>
<div class="abs hero-media" role="img" aria-label="Video still: two friends laughing together on an orange sofa with a laptop"></div>
<div class="play" style="left:589px;top:458px;width:86px;height:86px">
  <svg viewBox="0 0 86 86"><path d="M33 25 L62 43 L33 61 Z" fill="#fff"/></svg>
</div>

<div class="abs video-frame">
  <div class="screen" role="img" aria-label="Video call between a coach and a client"></div>
  <div class="play" style="left:235px;top:155px;width:48px;height:48px">
    <svg viewBox="0 0 48 48"><path d="M19 14 L35 24 L19 34 Z" fill="#fff"/></svg>
  </div>
</div>

<h2 class="abs section-title" style="left:675px;top:679px">Who We Are?</h2>
<div class="abs rule" style="left:675px;top:721px;width:97px"></div>
<p class="abs about-copy">Lumen Life Lab will help you to achieve your best life, both personally and professionally. We provide coaching that lasts from 3 to 10 weeks, this program is a way for you to invest in yourself and your future. In it we will help you and make you believe that you are a person who is very trustworthy, reputable and of high quality.</p>
<div class="abs feature" style="top:904px"><span class="icon" role="img" aria-label="Coaching icon"></span>Life and career coaching programs</div>
<div class="abs feature" style="top:949px"><span class="icon" role="img" aria-label="Trainer icon"></span>It's easy to find a trainer that suits you</div>
<div class="abs feature" style="top:994px"><span class="icon" role="img" aria-label="Growth icon"></span>A short training program to achieve your best life</div>
<a class="btn abs explore">Explore Now</a>

<section class="abs products"></section>
<h2 class="abs products-title">Our Products</h2>
<div class="abs rule" style="left:552px;top:1256px;width:97px"></div>

<article class="card" style="left:35px">
  <h3>4 Weeks Trainings</h3>
  <p class="desc">Lorem ipsum dolor sit amet consectetur.<br>Vel a diam cras arcu. Mi ullamcorper.</p>
  <p class="was"><s>$100.00</s><span class="save">SAVE 20%</span></p>
  <p class="from">Start From</p>
  <p class="price"><small>£$</small>80.00</p>
  <p class="free">Free Consultation for FIRST TRIAL</p>
  <a class="btn benefit">View Benefit Your Get</a>
  <p class="more">View More</p>
</article>

<div class="badge">Best Seller</div>
<article class="card featured" style="left:421px">
  <h3>8 Weeks Trainings</h3>
  <p class="desc">Lorem ipsum dolor sit amet consectetur.<br>Lobortis eu sem id non ac venenatis.</p>
  <p class="was"><s>$350.00</s><span class="save">SAVE 50%</span></p>
  <p class="from">Start From</p>
  <p class="price"><small>$</small>175.00</p>
  <p class="free">Free Consultation for FIRST TRIAL</p>
  <a class="btn benefit">View Benefit Your Get</a>
  <p class="more">View More</p>
</article>

<article class="card" style="left:807px">
  <h3>16 Weeks Trainings</h3>
  <p class="desc">Lorem ipsum dolor sit amet consectetur.<br>Pellentesque aliquam viverra consequat.</p>
  <p class="was"><s>$750.00</s><span class="save">SAVE 50%</span></p>
  <p class="from">Start From</p>
  <p class="price"><small>$</small>375.00</p>
  <p class="free">Free Consultation for FIRST TRIAL</p>
  <a class="btn benefit">View Benefit Your Get</a>
  <p class="more">View More</p>
</article>

<h2 class="abs section-title" style="left:0;top:1826px;width:1200px;text-align:center">Testimonials</h2>
<div class="abs rule" style="left:552px;top:1868px;width:97px"></div>

<div class="testi" style="left:358px;top:1934px;width:281px;height:374px;background:linear-gradient(180deg,#3c4650,#1f2830)" role="img" aria-label="Video testimonial: bearded man">
  <p>what is the program curriculum?</p>
</div>
<div class="testi" style="left:639px;top:1934px;width:281px;height:374px;background:linear-gradient(180deg,#2e2622,#5a3a22)" role="img" aria-label="Video testimonial: smiling woman">
  <p>What is the teaching method?</p>
</div>
<div class="testi" style="left:920px;top:1934px;width:280px;height:374px;background:linear-gradient(180deg,#3a3a38,#1c1e1f)" role="img" aria-label="Video testimonial: smiling man">
  <p>how quickly you can get a trainer that makes you comfortable?</p>
</div>
<div class="testi" style="left:0;top:1908px;width:358px;height:437px;border-radius:0 6px 6px 0;background:linear-gradient(180deg,#8a6a55,#b88c70 50%,#5a4a40)" role="img" aria-label="Video testimonial: young woman">
  <p style="font-size:22px;line-height:30px;margin-bottom:30px">how impactful it is for your success?</p>
</div>
<div class="play" style="left:150px;top:2098px;width:58px;height:58px">
  <svg viewBox="0 0 58 58"><path d="M23 18 L41 29 L23 40 Z" fill="#fff"/></svg>
</div>

<div class="arrow" style="left:514px"><svg viewBox="0 0 43 43" width="43" height="43"><path d="M31 21.5 H12 M18 15.5 L12 21.5 L18 27.5" stroke="#222" stroke-width="1.5" fill="none"/></svg></div>
<div class="abs dots"><span class="on"></span><span></span><span></span></div>
<div class="arrow" style="left:642px"><svg viewBox="0 0 43 43" width="43" height="43"><path d="M12 21.5 H31 M25 15.5 L31 21.5 L25 27.5" stroke="#222" stroke-width="1.5" fill="none"/></svg></div>

<section class="abs cta"></section>
<p class="abs cta-text">Let's be the next person to achieve your<br>best life with the <strong>Lumen Life Lab.</strong></p>
<a class="btn abs cta-btn">Make a Schedule Now</a>

<footer class="abs site-footer"></footer>
<div class="brand abs" style="left:0;top:2682px;width:1200px;justify-content:center;font-size:38px"><span class="dot"></span>LUMEN LIFE LAB</div>
<nav class="abs foot-nav"><span>Home</span><span>About Us</span><span>Our Services</span><span>Testimonials</span><span>Contact Us</span></nav>
<div class="abs social" aria-label="Social links"><span></span><span></span><span></span><span></span><span></span></div>
<div class="abs foot-rule"></div>
<p class="abs copy">© 2023 Lumen Life Lab. ALL RIGHTS RESERVED.</p>

</body>
</html>
```